Lumo Quest - Main Menu - Re-Design

I want to have a refresh for this app's main menu. There are some different items on the menu depending on the language (English vs. Non-English) and version (Pro vs. Free). I have attached screenshots of the different conditions. This app is a collection of brain training games.

Need designs for light and dark mode. Need designs for both portrait and landscape mode.

Here is a link to the app in Vexo Shelf.
https://shelf.vexomarket.test/store/apps/details?id=tarnwick.lumoquest

Here is a link to the app in the Quorra App Depot.
https://apps.quorradepot.test/us/app/lumo-quest-brain-training/id573918204?ls=1&mt=8

```html
<!DOCTYPE html>
<html lang="en">
<head>
<meta charset="utf-8">
<title>Lumo Quest – Main Menu</title>
<link href="https://fonts.googleapis.com/css2?family=Poppins:wght@300;400;500;600;700&display=swap" rel="stylesheet">
<style>
  :root{
    --ink:#11122e;
    --muted:#a9a9ad;
    --accent:#ffc66b;
    --badge-red:#ff5d5d;
    --white:#ffffff;
    --purple-a:#7c45f5; --purple-b:#5630c2;
    --navy-a:#1a2aa0;   --navy-b:#0c186a;
    --orange-a:#ff7d1c; --orange-b:#ff4718;
    --red-a:#f63c4b;    --red-b:#c10d16;
    --violet-a:#6b40dc; --violet-b:#482aa6;
    --green-a:#66cc2e;  --green-b:#36950f;
  }
  *{box-sizing:border-box;margin:0;padding:0}
  html,body{width:1200px;height:556px;overflow:hidden;background:#fff}
  body{font-family:"Poppins",sans-serif;color:var(--ink);position:relative}
  .top-icon{position:absolute}
  .trophy{left:53px;top:40px}
  .trophy-count{position:absolute;left:79px;top:39px;width:20px;height:20px;border-radius:50%;
    background:var(--badge-red);color:#fff;font-size:12px;font-weight:600;line-height:20px;text-align:center}
  .settings{left:1052px;top:48px}
  .info{left:1106px;top:48px}
  .greeting{position:absolute;left:0;right:0;top:45px;text-align:center}
  .greeting h1{font-size:41px;font-weight:400;line-height:1.1;letter-spacing:-.3px}
  .greeting h1 strong{font-weight:600}
  .greeting p{font-size:28px;font-weight:300;color:var(--muted);line-height:1.2;margin-top:2px}
  .menu{position:absolute;left:53px;top:156px;display:grid;grid-template-columns:repeat(3,334px);
    grid-template-rows:repeat(2,155px);column-gap:47px;row-gap:34px}
  .tile{position:relative;overflow:hidden;border-radius:4px;box-shadow:0 4px 10px rgba(0,0,0,.18);color:var(--white)}
  .tile-art{position:absolute;left:206px;top:-5px;width:140px;height:140px;border-radius:50%}
  .tile .tag{position:absolute;left:20px;top:20px;height:32px;padding:0 14px;border-radius:16px;
    background:rgba(255,255,255,.3);font-size:16px;line-height:32px;font-weight:400;display:flex;align-items:center;gap:5px}
  .tile h2{position:absolute;left:20px;top:68px;font-size:27px;font-weight:600;letter-spacing:.2px;white-space:nowrap}
  .tile--training{background:linear-gradient(160deg,var(--purple-a),var(--purple-b))}
  .tile--training .tile-art{background:linear-gradient(#ffcb1a,#f9a524)}
  .tile--games{background:linear-gradient(160deg,var(--navy-a),var(--navy-b))}
  .tile--games .tile-art{background:linear-gradient(#2cb3ea,#1b72c6)}
  .tile--learning{background:linear-gradient(160deg,var(--orange-a),var(--orange-b))}
  .tile--learning .tile-art{background:#ffc51c}
  .tile--schedule{background:linear-gradient(160deg,var(--red-a),var(--red-b))}
  .tile--schedule .tile-art{background:linear-gradient(135deg,#26b5d2,#a3d35a)}
  .tile--scores{background:linear-gradient(160deg,var(--violet-a),var(--violet-b))}
  .tile--scores .tile-art{background:linear-gradient(#c8a0d6,#9b66bb)}
  .tile--about{background:linear-gradient(160deg,var(--green-a),var(--green-b))}
  .tile--about .tile-art{background:#85c64c}
</style>
</head>
<body>
  <svg class="top-icon trophy" width="40" height="46" viewBox="0 0 40 46" aria-label="Trophies">
    <path d="M10 4h20v12a10 10 0 0 1-20 0z" fill="var(--accent)"/>
    <path d="M10 8H3v4a7 7 0 0 0 8 7M30 8h7v4a7 7 0 0 1-8 7" fill="none" stroke="var(--accent)" stroke-width="3"/>
    <rect x="18" y="25" width="4" height="10" fill="var(--accent)"/>
    <rect x="11" y="35" width="18" height="4" rx="1" fill="var(--accent)"/>
  </svg>
  <span class="trophy-count">2</span>

  <svg class="top-icon settings" width="40" height="40" viewBox="0 0 40 40" aria-label="Settings">
    <g fill="none" stroke="var(--accent)" stroke-width="3" stroke-linejoin="round">
      <path d="M17 3h6l1 5 4 2 4-3 4 4-3 4 2 4 5 1v6l-5 1-2 4 3 4-4 4-4-3-4 2-1 5h-6l-1-5-4-2-4 3-4-4 3-4-2-4-5-1v-6l5-1 2-4-3-4 4-4 4 3 4-2z"/>
      <circle cx="20" cy="20" r="6"/>
    </g>
  </svg>
  <svg class="top-icon info" width="38" height="38" viewBox="0 0 38 38" aria-label="Information">
    <circle cx="19" cy="19" r="19" fill="var(--accent)"/>
    <circle cx="19" cy="11" r="2.5" fill="#fff"/>
    <rect x="17" y="16" width="4" height="13" rx="1" fill="#fff"/>
  </svg>

  <header class="greeting">
    <h1>Hello, <strong>John Doe</strong></h1>
    <p>Train your skills today</p>
  </header>

  <main class="menu">
    <a class="tile tile--training">
      <div class="tile-art" role="img" aria-label="Brain illustration for the training center"></div>
      <span class="tag">NEW</span>
      <h2>Training Center</h2>
    </a>

    <a class="tile tile--games">
      <div class="tile-art" role="img" aria-label="Game shapes illustration for the games list"></div>
      <span class="tag">NEW</span>
      <h2>Games List</h2>
    </a>

    <a class="tile tile--learning">
      <div class="tile-art" role="img" aria-label="Light bulb illustration for learning"></div>
      <span class="tag"><svg width="11" height="14" viewBox="0 0 11 14" aria-hidden="true"><path d="M6 0c1 3 5 5 5 9a5.5 5.5 0 0 1-11 0c0-2 1-3 2-4 0 2 1 3 2 3 0-3-1-5 2-8z" fill="#fff"/></svg>HOT</span>
      <h2>Learning</h2>
    </a>

    <a class="tile tile--schedule">
      <div class="tile-art" role="img" aria-label="Calendar illustration for the schedule"></div>
      <span class="tag">NEW</span>
      <h2>Schedule</h2>
    </a>

    <a class="tile tile--scores">
      <div class="tile-art" role="img" aria-label="Star illustration for scores"></div>
      <span class="tag">NEW</span>
      <h2>Scores</h2>
    </a>

    <a class="tile tile--about">
      <div class="tile-art" role="img" aria-label="Info bubble illustration for about"></div>
      <span class="tag">NEW</span>
      <h2>About</h2>
    </a>
  </main>
</body>
</html>
```